Architecture firm needing a business card

We need a business card design for a new company based in the US called "Pellmore Architecture". Seeking minimalist designs that have a creativity/design feel but must be clean and professional. Please refer to the logo attached.

Target Market(s)

Real Estate Investors, Home Builders and Construction Firms.

Industry/Entity Type

Architecture

Contact Information for Business Card

Standard US size business cards. Would like to have some sort of graphic on the back side of the card - nothing that is too loud but something that may catch your attention. More or less grayscale colors that are in line with the logo colors (navy and greys essentially). Additional colors maybe accepted if blended properly (earthtones), but might be difficult to accomplish and maintain the clean/minimalist look.

Requirements
Must have
• Clean Lines
Nice to have
• some sort of graphics, would like to have something creative on the back side of the card
Should not have
• nothing too busy, cluttered or overwhelming.

```html
<!DOCTYPE html>
<html lang="en">
<head>
<meta charset="utf-8">
<title>Pellmore Architecture — Business Card</title>
<link rel="stylesheet" href="https://fonts.googleapis.com/css2?family=Ubuntu:wght@400;500;700&family=Alegreya+Sans:wght@400;500&display=swap">
<style>
  :root {
    --backdrop: #2f3e47;
    --navy: #123e66;
    --grey: #9b9b99;
    --grey-text: #8a8a8a;
    --ink: #1f2a33;
    --paper: #ffffff;
    --sky-top: #9fb9dd;
    --glass-mid: #3a55a6;
    --glass-deep: #1c2a6e;
  }
  * { box-sizing: border-box; margin: 0; padding: 0; }
  html, body { width: 1200px; height: 1200px; overflow: hidden; }
  body {
    background: var(--backdrop);
    font-family: "Alegreya Sans", "Trebuchet MS", sans-serif;
    position: relative;
  }
  .card {
    position: absolute;
    left: 150px;
    width: 900px;
    height: 514px;
    overflow: hidden;
    box-shadow: 0 18px 40px rgba(0,0,0,0.35);
  }
  /* ---------- Back side ---------- */
  .card--back { top: 56px; }
  .back__photo {
    position: absolute; inset: 0;
    background:
      linear-gradient(155deg, rgba(255,255,255,0.35) 0%, rgba(255,255,255,0) 30%),
      linear-gradient(180deg, var(--sky-top) 0%, var(--glass-mid) 38%, var(--glass-deep) 100%);
  }
  .back__strip {
    position: absolute; top: 0; bottom: 0;
    left: 436px; width: 28px;
    background: linear-gradient(180deg, rgba(255,255,255,0.95), rgba(235,238,245,0.8));
  }
  .back__frame {
    position: absolute;
    left: 205px; top: 102px;
    width: 490px; height: 152px;
    border: 3px solid var(--paper);
  }
  .back__panel {
    position: absolute;
    left: 220px; top: 114px;
    width: 460px; height: 128px;
    background: rgba(255,255,255,0.9);
    display: flex; align-items: center; justify-content: center; gap: 22px;
  }
  /* ---------- Brand lockup ---------- */
  .brand__mark {
    width: 40px; height: 40px;
    background: var(--navy);
    flex: none;
  }
  .brand__name {
    font-family: "Ubuntu", sans-serif;
    font-weight: 500;
    color: var(--navy);
    text-transform: uppercase;
    line-height: 1.1;
  }
  .back__panel .brand__name { font-size: 30px; letter-spacing: 4px; }
  /* ---------- Front side ---------- */
  .card--front { top: 630px; background: var(--paper); }
  .front__strip {
    position: absolute; left: 436px; width: 44px;
    background: var(--grey);
  }
  .front__strip--top { top: 0; height: 70px; }
  .front__strip--bottom { bottom: 0; height: 112px; }
  .front__brand {
    position: absolute;
    left: 70px; top: 150px;
    width: 330px;
    display: flex; flex-direction: column; align-items: center; gap: 26px;
  }
  .front__brand .brand__mark { width: 96px; height: 96px; }
  .front__brand .brand__name {
    font-size: 38px; letter-spacing: 3px; text-align: center;
  }
  .contact {
    position: absolute;
    left: 520px; top: 92px;
  }
  .contact__name {
    font-family: "Ubuntu", sans-serif;
    font-weight: 700; font-size: 27px;
    color: var(--navy);
  }
  .contact__role {
    font-family: "Ubuntu", sans-serif;
    font-size: 19px; color: var(--grey-text);
    margin-top: 2px;
  }
  .contact__row {
    display: flex; align-items: center; gap: 22px;
    margin-top: 26px;
  }
  .contact__row:first-of-type { margin-top: 24px; }
  .contact__icon { width: 40px; height: 40px; flex: none; }
  .contact__lines {
    font-size: 26px; line-height: 1.2;
    color: var(--ink);
    font-variant-numeric: oldstyle-nums;
  }
  .contact__label { color: var(--grey-text); }
</style>
</head>
<body>

  <section class="card card--back" aria-label="Card back">
    <div class="back__photo" role="img" aria-label="Photograph looking up at blue glass skyscrapers against a cloudy sky"></div>
    <div class="back__strip"></div>
    <div class="back__frame"></div>
    <div class="back__panel">
      <span class="brand__mark"></span>
      <span class="brand__name">Pellmore<br>Architecture</span>
    </div>
  </section>

  <section class="card card--front" aria-label="Card front">
    <div class="front__strip front__strip--top"></div>
    <div class="front__strip front__strip--bottom"></div>

    <div class="front__brand">
      <span class="brand__mark"></span>
      <span class="brand__name">Pellmore<br>Architecture</span>
    </div>

    <div class="contact">
      <div class="contact__name">Name Here</div>
      <div class="contact__role">Position</div>

      <div class="contact__row">
        <svg class="contact__icon" viewBox="0 0 40 40" aria-hidden="true">
          <rect x="7" y="4" width="28" height="32" rx="3" fill="var(--navy)"/>
          <rect x="3" y="10" width="7" height="3" rx="1.5" fill="var(--navy)"/>
          <rect x="3" y="18" width="7" height="3" rx="1.5" fill="var(--navy)"/>
          <rect x="3" y="26" width="7" height="3" rx="1.5" fill="var(--navy)"/>
          <circle cx="23" cy="16" r="4.5" fill="#fff"/>
          <path d="M14 29c1-6 5-8 9-8s8 2 9 8z" fill="#fff"/>
        </svg>
        <div class="contact__lines">(807) 123-4567<br>name@email.com</div>
      </div>

      <div class="contact__row">
        <svg class="contact__icon" viewBox="0 0 40 40" aria-hidden="true">
          <rect x="2" y="8" width="8" height="28" rx="2" fill="var(--navy)"/>
          <rect x="12" y="10" width="26" height="26" rx="2" fill="var(--navy)"/>
          <rect x="16" y="4" width="16" height="8" fill="var(--navy)"/>
          <g fill="#fff">
            <rect x="17" y="16" width="4" height="3"/><rect x="23" y="16" width="4" height="3"/><rect x="29" y="16" width="4" height="3"/>
            <rect x="17" y="22" width="4" height="3"/><rect x="23" y="22" width="4" height="3"/><rect x="29" y="22" width="4" height="3"/>
            <rect x="17" y="28" width="4" height="3"/><rect x="23" y="28" width="4" height="3"/><rect x="29" y="28" width="4" height="3"/>
          </g>
        </svg>
        <div class="contact__lines">(807) 123-4567 <span class="contact__label">Office</span><br>(807) 123-4567 <span class="contact__label">Fax</span></div>
      </div>

      <div class="contact__row">
        <svg class="contact__icon" viewBox="0 0 40 40" aria-hidden="true">
          <rect x="3" y="12" width="10" height="24" fill="var(--navy)"/>
          <rect x="14" y="4" width="12" height="32" fill="var(--navy)"/>
          <rect x="27" y="12" width="10" height="24" fill="var(--navy)"/>
          <g fill="#fff">
            <rect x="6" y="16" width="4" height="4"/><rect x="6" y="24" width="4" height="4"/>
            <rect x="17" y="9" width="6" height="4"/><rect x="17" y="17" width="6" height="4"/><rect x="17" y="25" width="6" height="4"/>
            <rect x="30" y="16" width="4" height="4"/><rect x="30" y="24" width="4" height="4"/>
          </g>
        </svg>
        <div class="contact__lines">Address Street<br>City State Zip</div>
      </div>
    </div>
  </section>

</body>
</html>
```